Affiliate website design and wireframe

We need a design of an affiliate website for an application we purchased, it is important that you build the website pages according to the developer of the applications specifications (please see attached documents) the developer of the application will configure the pages and add them to the site. Please take special note of his comments below.

We all so need you to create a wire frame so the developer can test everything (http://quartz.lomeriva.vn/)

It will be the homepage and about 16 inner pages (please see attached files)
Here is our website http://maplecourtlink.com/affiliate/affiliates/index.php

The version of the software we purchased is the Quill Partner Grid version

Comments from the developers

1. I will need the source files of the design (photoshop .psd files and font files if custom fonts are used), since the implementation is closely bound to component sizes (like border width, margin width etc.) and colors. If you own a corporate design manual, it's crucial to send it as well. Also, please, make sure if you use custom fonts, that these allow legal website integration (like zorvix web fonts).

2. Any and every content is controlled via templates. All editing/adding/removing etc. is done here. The template files are essentially html/php documents, they use a template engine called brisko (http://www.brisko.net/) which has it's own language similar to php.

3. .psd files are ideal, because we deal with the specifics of QPS/QPG implementation on a daily basis. Any html/css developed in advance may prove to be a poor choice. You may choose to let an in-house developer do the job, but experience wise this is more costly, since he will not be accustomed to the template/functionality systems of QPS/QPG.

4. I will need the source files of the design (photoshop .psd files and font files if custom fonts are used), since the implementation is closely bound to component sizes (like border width, margin width etc.) and colors. If you own a corporate design manual, it's crucial to send it as well. Also, please, make sure if you use custom fonts, that these allow legal website integration (like zorvix web fonts).

Regards,

Tomas Vereck

We prefer illustrations more than pictures of real people.

This is the home page, it is asking for Merchant and Affiliate sign up, not just affiliate.

http://maplecourtlink.com/affiliate/index.php

Please note the home page features both Merchant and Affiliate sign up

We are looking for illustration design not just stock images

Please remember the search menu that searches for the available programs, see the example we gave you, look at the search menu at the top of the page http://www.tradolink.com/

We are reviewing everything, no need to send more designs

Target Market(s)

Natural Products Manufacturers
Natural products Sales reps
Natural Products Bloggers
Social Marketing

Industry/Entity Type

Software

Requirements
Must have
• 1. All links on pages should go to the appropriate pages.
2. Colors can be based on our logo design (look at the attachments)
3. Here is our website http://maplecourtlink.com/affiliate/affiliates/index.php
4. We have attached a drawing of how we think the homepage concept should follow.
5. Main concept of design, is trying to show our sales people (Affiliates) are doing multiple things to advertise and sell the merchants products.(see logo)
6. Need to be able to edit all text and images.
7. Our target audience is Natural product sales people (Advertisers, bloggers, ext) and natural product manufacturers.
8. You can speak to the company who made the application, through live chat, on there website http://www.quillpartnergrid.com/
Nice to have
• See Attached Documents.
site should take up whole website pages
Look For fun Illustrated Website, one of the better ones we have seen is http://www.tradolink.com/index.cfm
Should not have
• Please look very carefully at developers comment above.

```html
<!DOCTYPE html>
<html lang="en">
<head>
<meta charset="utf-8">
<title>Maplecourt Link – Affiliate Program</title>
<link rel="stylesheet" href="https://fonts.googleapis.com/css2?family=Open+Sans:wght@400;600;700&family=Roboto+Condensed:wght@400;700&display=swap">
<style>
:root{
  --navy:#123a6b;
  --navy-dark:#0d2d58;
  --blue:#1f5d94;
  --green:#4f9a12;
  --green-bright:#76c225;
  --green-dark:#3f8a0c;
  --text:#2b2b2b;
  --muted:#666;
  --white:#fff;
  --line:#d5d9de;
}
*{margin:0;padding:0;box-sizing:border-box}
html,body{width:1009px;height:1200px;overflow:hidden;background:var(--white)}
body{position:relative;font-family:"Open Sans",Arial,sans-serif;color:var(--text)}
a{color:inherit;text-decoration:none}
.abs{position:absolute}

/* header */
.brand{left:106px;top:36px;display:flex;align-items:center;gap:10px}
.brand-dot{width:30px;height:30px;border-radius:50%;background:var(--green)}
.brand-name{font-family:"Roboto Condensed",sans-serif;font-weight:700;font-size:26px;color:var(--navy);letter-spacing:.5px}
.top-btn{top:29px;height:29px;line-height:29px;color:var(--white);font-size:13px;font-style:italic;font-weight:600;text-align:center}
.top-btn.affiliate{left:672px;width:104px;background:linear-gradient(#6cbf1c,#4c9a10)}
.top-btn.merchant{left:790px;width:113px;background:linear-gradient(#2f5e8e,#1c4674)}
.main-nav{top:84px;left:424px;display:flex;gap:0;font-size:14px;font-weight:600;color:#555}
.main-nav a{position:absolute;white-space:nowrap}
.main-nav a.active{color:var(--navy)}

/* hero */
.hero-left{left:0;top:112px;width:505px;height:345px;background:radial-gradient(ellipse at 20% 40%,#8fd24a 0%,#62b224 45%,#3f9016 100%)}
.hero-right{left:505px;top:112px;width:504px;height:345px;background:radial-gradient(ellipse at 70% 30%,#3a7ab2 0%,#1f568c 50%,#123f70 100%)}
.hero-title{font-family:"Roboto Condensed",sans-serif;font-size:31px;color:var(--white);top:172px;letter-spacing:-.3px}
.hero-text{color:var(--white);font-size:14.5px;font-weight:600;line-height:23px;top:233px;width:340px}
.hero-btn{top:338px;height:50px;line-height:50px;text-align:center;font-family:"Roboto Condensed",sans-serif;font-size:24px;color:var(--white)}
.hero-btn.signup{left:106px;width:240px;background:linear-gradient(90deg,#102f5e,#2c5c8e)}
.hero-btn.login{left:581px;width:228px;background:linear-gradient(#86d33a,#5aa81a)}
.hero-shadow{left:120px;top:457px;width:780px;height:22px;background:radial-gradient(ellipse at 50% 0%,rgba(0,0,0,.18),rgba(0,0,0,0) 70%)}

/* welcome */
.welcome-title{left:104px;top:484px;font-size:19.5px;font-weight:700;color:var(--navy)}
.welcome-title .accent{color:var(--green)}
.welcome-rule{left:104px;top:514px;width:790px;height:1px;background:var(--line)}
.link-icon{left:880px;top:494px}
.intro{left:104px;width:802px;font-size:12.6px;line-height:19.2px;color:#333}
.intro h3{font-size:13px;font-weight:600;color:var(--navy);margin-bottom:1px}
.intro.one{top:520px}
.intro.two{top:589px}

/* feature cards */
.card{top:676px;width:178px;height:260px;background:var(--white);border:3px solid var(--green);border-radius:4px;box-shadow:inset 0 0 14px rgba(0,0,0,.12),0 6px 10px rgba(0,0,0,.06);text-align:center}
.card.navy{border-color:var(--navy)}
.card-badge{position:absolute;left:44px;top:-3px;width:90px;height:45px;border-radius:0 0 45px 45px;background:var(--green);display:flex;justify-content:center;padding-top:8px}
.card.navy .card-badge{background:var(--navy)}
.card-title{position:absolute;left:0;right:0;top:58px;font-family:"Roboto Condensed",sans-serif;font-size:17px;line-height:19px;color:var(--navy)}
.card-sub{position:absolute;left:0;right:0;top:91px;font-family:"Roboto Condensed",sans-serif;font-weight:700;font-size:12px;color:var(--navy)}
.card-body{position:absolute;left:12px;right:12px;top:128px;font-size:11.2px;line-height:17.5px;color:var(--navy)}
.card-tip{position:absolute;left:72px;bottom:-19px}
.slider-arrow{top:782px}

/* footer */
.footer-green{left:0;top:986px;width:505px;height:176px;background:linear-gradient(180deg,#5ba812,#3e8a0d)}
.footer-blue{left:505px;top:986px;width:504px;height:176px;background:linear-gradient(180deg,#163f72,#0e2e5b)}
.footer-col{top:1005px}
.footer-col h4{font-weight:400;font-size:13.5px;margin-bottom:6px}
.footer-green .footer-col h4,.footer-col.on-green h4{color:var(--navy)}
.footer-col.on-blue h4{color:#a6d84a}
.footer-col ul{list-style:none;font-size:10.5px;line-height:17.6px;color:var(--white)}
.footer-col ul li::before{content:"› ";}
.footer-col.social ul li{line-height:24px;display:flex;align-items:center;gap:7px}
.footer-col.social ul li::before{content:none}
.social-dot{width:20px;height:20px;border-radius:50%;background:#0b0b0b;display:inline-block}
.footer-divider{top:986px;width:1px;height:176px;background:rgba(255,255,255,.12)}
.copyright{left:0;top:1174px;width:1009px;text-align:center;font-size:10px;color:var(--navy)}
</style>
</head>
<body>

<header>
  <a class="brand abs" href="#"><span class="brand-dot"></span><span class="brand-name">Maplecourt Link</span></a>
  <a class="top-btn affiliate abs" href="#">Affiliate login</a>
  <a class="top-btn merchant abs" href="#">Merchant login</a>
  <nav class="main-nav abs">
    <a class="active" href="#" style="left:0">HOME</a>
    <a href="#" style="left:64px">ABOUT US</a>
    <a href="#" style="left:154px">POPULER</a>
    <a href="#" style="left:238px">BUSINESS</a>
    <a href="#" style="left:325px">SING UP</a>
    <a href="#" style="left:403px">CONTACT US</a>
  </nav>
</header>

<section class="hero">
  <div class="hero-left abs" role="img" aria-label="Green illustrated backdrop of social marketing icons and a sales rep"></div>
  <div class="hero-right abs" role="img" aria-label="Blue illustrated backdrop of a business person and growth charts"></div>
  <h1 class="hero-title abs" style="left:104px">START MAKING MONEY NOW!</h1>
  <p class="hero-text abs" style="left:104px">There is no charge to join our Affiliate Program. We pay commissions for all sales you referred. Earn up to 30% commissions</p>
  <a class="hero-btn signup abs" href="#">AFFILIATES SIGNUP</a>
  <h1 class="hero-title abs" style="left:580px">ALREADY OUR AFFILIATE?</h1>
  <p class="hero-text abs" style="left:581px;width:330px">We have always something new for our affiliates. Login to check earned commissions and new campaigns.</p>
  <a class="hero-btn login abs" href="#">AFFILIATES LOGIN</a>
  <div class="hero-shadow abs"></div>
</section>

<section class="welcome">
  <h2 class="welcome-title abs">Welcome to <span class="accent">Maplecourt</span> Link</h2>
  <div class="welcome-rule abs"></div>
  <svg class="link-icon abs" width="26" height="20" viewBox="0 0 26 20"><g fill="none" stroke="#9aa2ab" stroke-width="2"><rect x="2" y="7" width="12" height="7" rx="3.5" transform="rotate(-35 8 10)"/><rect x="12" y="5" width="12" height="7" rx="3.5" transform="rotate(-35 18 8)"/></g></svg>
  <div class="intro one abs">
    <h3>Earn up to 50% commission for all products!</h3>
    <p>Not only can you join our team and help spread the word about your favorite products, you can get rewarded for your efforts. Our system tracks referrals and pays top commissions for every client you send our way.</p>
  </div>
  <div class="intro two abs">
    <h3>High Conversion Rate = More Money.</h3>
    <p>Our website and plans generate one of the highest conversion rates in the industry. Our high conversion rates mean that the people who you send here are more likely to buy our products. Of course we can't prove that either, but if you don't trust us, why would you want to refer people here?</p>
  </div>
</section>

<section class="features">
  <svg class="slider-arrow abs" style="left:106px" width="10" height="22" viewBox="0 0 10 22"><path d="M10 0 L0 11 L10 22Z" fill="var(--navy)"/></svg>
  <svg class="slider-arrow abs" style="left:894px" width="10" height="22" viewBox="0 0 10 22"><path d="M0 0 L10 11 L0 22Z" fill="var(--green)"/></svg>

  <article class="card navy abs" style="left:128px">
    <div class="card-badge"><svg width="30" height="26" viewBox="0 0 30 26"><g fill="none" stroke="#fff" stroke-width="2.4"><rect x="3" y="7" width="24" height="16"/><path d="M3 7 L15 16 L27 7"/></g></svg></div>
    <h3 class="card-title">Email Marketing</h3>
    <p class="card-sub">Easliy Execute Great Campaigns</p>
    <p class="card-body">Lorem ipsum dolor sit amet, consectetur adipiscing elit. Praesent auctor sagittis dignissim. Praesent urna orci, mattis ut quam eu, sodales rhoncus turpis.</p>
    <svg class="card-tip" width="28" height="19" viewBox="0 0 28 19"><path d="M0 0 L14 17 L28 0" fill="#fff" stroke="var(--navy)" stroke-width="3"/></svg>
  </article>

  <article class="card abs" style="left:319px">
    <div class="card-badge"><svg width="34" height="26" viewBox="0 0 34 26" fill="#fff"><circle cx="9" cy="9" r="4"/><circle cx="25" cy="9" r="4"/><circle cx="17" cy="7" r="5"/><path d="M2 23 q7-12 14 0Z"/><path d="M18 23 q7-12 14 0Z"/><path d="M9 24 q8-14 16 0Z"/></svg></div>
    <h3 class="card-title">Lead Management</h3>
    <p class="card-sub">Get the right leads to sales</p>
    <p class="card-body">Lorem ipsum dolor sit amet, consectetur adipiscing elit. Praesent auctor sagittis dignissim. Praesent urna orci, mattis ut quam eu, sodales rhoncus turpis.</p>
    <svg class="card-tip" width="28" height="19" viewBox="0 0 28 19"><path d="M0 0 L14 17 L28 0" fill="#fff" stroke="var(--green)" stroke-width="3"/></svg>
  </article>

  <article class="card abs" style="left:512px">
    <div class="card-badge"><svg width="30" height="26" viewBox="0 0 30 26"><rect x="3" y="3" width="24" height="16" fill="none" stroke="#fff" stroke-width="2.4"/><rect x="12" y="19" width="6" height="4" fill="#fff"/><rect x="8" y="23" width="14" height="2" fill="#fff"/><path d="M13 7 L13 15 L15 13 L17 16 L18 15 L16 12 L19 12Z" fill="#fff"/></svg></div>
    <h3 class="card-title">Website Analytics</h3>
    <p class="card-sub">From click to customer</p>
    <p class="card-body">Lorem ipsum dolor sit amet, consectetur adipiscing elit. Praesent auctor sagittis dignissim. Praesent urna orci, mattis ut quam eu,</p>
    <svg class="card-tip" width="28" height="19" viewBox="0 0 28 19"><path d="M0 0 L14 17 L28 0" fill="#fff" stroke="var(--green)" stroke-width="3"/></svg>
  </article>

  <article class="card abs" style="left:703px">
    <div class="card-badge"><svg width="30" height="28" viewBox="0 0 30 28"><g fill="none" stroke="#fff" stroke-width="2.4"><circle cx="14" cy="15" r="11"/><circle cx="14" cy="15" r="6"/></g><circle cx="14" cy="15" r="2" fill="#fff"/><path d="M14 15 L26 3" stroke="#fff" stroke-width="2.4"/></svg></div>
    <h3 class="card-title">Integrated Sales &amp;<br>Marketing CRM</h3>
    <p class="card-sub" style="top:109px">All your information&nbsp; in one place</p>
    <p class="card-body" style="top:128px">Lorem ipsum dolor sit amet, consectetur adipiscing elit. Praesent auctor sagittis dignissim. Praesent urna orci, mattis ut quam eu, sodales rhoncus turpis.</p>
    <svg class="card-tip" width="28" height="19" viewBox="0 0 28 19"><path d="M0 0 L14 17 L28 0" fill="#fff" stroke="var(--green)" stroke-width="3"/></svg>
  </article>
</section>

<footer>
  <div class="footer-green abs"></div>
  <div class="footer-blue abs"></div>
  <div class="footer-divider abs" style="left:205px"></div>
  <div class="footer-divider abs" style="left:345px"></div>
  <div class="footer-divider abs" style="left:640px"></div>
  <div class="footer-divider abs" style="left:740px"></div>

  <div class="footer-col on-green abs" style="left:110px"><h4>Main Links</h4><ul><li>Home</li><li>About Us</li><li>Product</li><li>Blog</li><li>Resoucces</li><li>Solutions</li></ul></div>
  <div class="footer-col on-green abs" style="left:239px"><h4>Partners</h4><ul><li>Resoucces</li><li>Agency partners</li><li>CRM Partners</li><li>Become a partner</li></ul></div>
  <div class="footer-col on-green abs" style="left:379px"><h4>Support</h4><ul><li>Contact Support</li><li>FAQs</li><li>Tutorials on Demand</li><li>Documentation</li></ul></div>
  <div class="footer-col on-blue abs" style="left:527px"><h4>Sitemap</h4><ul><li>Privacy</li><li>Cookies</li><li>Terms &amp; Conditions</li></ul></div>
  <div class="footer-col on-blue social abs" style="left:661px"><h4>Follows</h4><ul><li><span class="social-dot"></span>Facetome</li><li><span class="social-dot"></span>Chirper</li><li><span class="social-dot"></span>Rss</li><li><span class="social-dot"></span>Zorvix+</li><li><span class="social-dot"></span>Linkvane</li></ul></div>
  <div class="footer-col on-blue abs" style="left:766px"><h4>Resources</h4><ul><li>Merchants Login</li><li>Integration methods</li><li>API Reference</li><li>Samples and Tests</li><li>Quill Partner Pro</li></ul></div>

  <p class="copyright abs">Copyright © 2013 Maplecourt Link. All rights reserved.</p>
</footer>

</body>
</html>
```